Business Card + Letterhead Design for KESTOVA TRADING INC.

We already have a logo; now we need a business card + letterhead. We import and distribute flags and souvenirs with an emphasis on soccer related memorabilia. We target various ethnic markets and sporting goods stores. "International Souvenirs"

```html
<!DOCTYPE html>
<html lang="en">
<head>
<meta charset="utf-8">
<title>Kestova Trading Inc. — Business Card &amp; Letterhead</title>
<link href="https://fonts.googleapis.com/css2?family=Arimo:wght@400;700&display=swap" rel="stylesheet">
<style>
  :root {
    --backdrop: #5a0606;
    --brand-red: #7a1414;
    --ink: #111111;
    --text: #333333;
    --muted: #666666;
    --paper: #ffffff;
  }
  * { box-sizing: border-box; margin: 0; padding: 0; }
  html, body { width: 900px; height: 1200px; overflow: hidden; }
  body {
    background: var(--backdrop);
    font-family: "Arimo", Arial, sans-serif;
    color: var(--text);
    position: relative;
  }
  .wordmark {
    font-family: "Arimo", Arial, sans-serif;
    font-weight: 700;
    color: var(--brand-red);
    letter-spacing: 1px;
    display: flex;
    align-items: center;
    gap: 6px;
    white-space: nowrap;
  }
  .wordmark .dot {
    width: 14px; height: 14px; border-radius: 50%;
    background: var(--brand-red); flex: none;
  }

  /* Business card — front */
  .card {
    position: absolute;
    width: 190px; height: 300px;
    border-radius: 10px;
    overflow: hidden;
  }
  .card-front {
    left: 230px; top: 60px;
    background: var(--ink);
    display: flex; align-items: center; justify-content: center;
  }
  .card-front .wordmark { color: var(--paper); font-size: 15px; }
  .card-front .wordmark .dot { background: var(--paper); }

  /* Business card — back */
  .card-back {
    left: 470px; top: 60px;
    background: var(--paper);
    padding: 18px 14px 0;
  }
  .card-back .wordmark { font-size: 13px; }
  .card-back .person {
    margin-top: 16px;
    font-size: 11px; font-weight: 700; color: var(--ink);
  }
  .contact-list { list-style: none; margin-top: 10px; }
  .contact-list li {
    display: flex; align-items: center; gap: 6px;
    font-size: 8px; line-height: 14px; color: var(--text);
  }
  .contact-list svg { width: 9px; height: 9px; flex: none; }
  .card-back .dark-band {
    position: absolute; left: 0; right: 0; top: 170px; height: 80px;
    background: var(--ink);
  }
  .tagline {
    position: absolute;
    background: var(--brand-red); color: var(--paper);
    font-size: 8px; padding: 3px 8px;
  }
  .card-back .tagline { right: 0; top: 256px; }
  .card-back .web {
    position: absolute; right: 10px; top: 278px;
    font-size: 8px; color: var(--text);
  }

  /* Letterhead */
  .letterhead {
    position: absolute;
    left: 170px; top: 410px;
    width: 560px; height: 750px;
    background: var(--paper);
  }
  .letterhead .corner-block {
    position: absolute; left: 0; top: 0;
    width: 90px; height: 62px; background: var(--ink);
  }
  .letterhead .head-brand {
    position: absolute; left: 140px; top: 16px;
  }
  .letterhead .head-brand .wordmark { font-size: 16px; }
  .letterhead .address {
    position: absolute; left: 140px; top: 64px;
    font-size: 7px; color: var(--muted);
  }
  .letterhead .rule {
    position: absolute; left: 120px; right: 14px; top: 58px;
    height: 1px; background: var(--brand-red);
  }
  .letterhead .contact-list {
    position: absolute; right: 18px; top: 2px; margin: 0;
  }
  .letterhead .contact-list li { font-size: 7px; line-height: 12px; }
  .letterhead .tagline {
    right: 0; bottom: 22px; font-size: 10px; padding: 6px 18px 6px 22px;
  }
</style>
</head>
<body>

  <section class="card card-front" aria-label="Business card front">
    <div class="wordmark"><span class="dot"></span>KESTOVA TRADING</div>
  </section>

  <section class="card card-back" aria-label="Business card back">
    <div class="wordmark"><span class="dot"></span>KESTOVA TRADING</div>
    <p class="person">Daniel Morrow</p>
    <ul class="contact-list">
      <li><svg viewBox="0 0 10 10"><path d="M2 1h2l1 2-1.2 1a5 5 0 0 0 2.2 2.2L7 5l2 1v2a1 1 0 0 1-1 1A7 7 0 0 1 1 2a1 1 0 0 1 1-1z" fill="#7a1414"/></svg>(647) 555-0182</li>
      <li><svg viewBox="0 0 10 10"><path d="M2 1h2l1 2-1.2 1a5 5 0 0 0 2.2 2.2L7 5l2 1v2a1 1 0 0 1-1 1A7 7 0 0 1 1 2a1 1 0 0 1 1-1z" fill="#7a1414"/></svg>(866) 555-0147</li>
      <li><svg viewBox="0 0 10 10"><rect x="1" y="2.5" width="8" height="5.5" fill="none" stroke="#7a1414"/><path d="M1 2.5l4 3 4-3" fill="none" stroke="#7a1414"/></svg>sales@kestovatrading.ca</li>
    </ul>
    <div class="dark-band"></div>
    <div class="tagline">International Flags &amp; Souvenirs</div>
    <div class="web">www.kestovatrading.ca</div>
  </section>

  <section class="letterhead" aria-label="Letterhead">
    <div class="corner-block"></div>
    <div class="head-brand">
      <div class="wordmark"><span class="dot"></span>KESTOVA TRADING</div>
    </div>
    <ul class="contact-list">
      <li><svg viewBox="0 0 10 10"><path d="M2 1h2l1 2-1.2 1a5 5 0 0 0 2.2 2.2L7 5l2 1v2a1 1 0 0 1-1 1A7 7 0 0 1 1 2a1 1 0 0 1 1-1z" fill="#7a1414"/></svg>(647) 555-0182</li>
      <li><svg viewBox="0 0 10 10"><path d="M2 1h2l1 2-1.2 1a5 5 0 0 0 2.2 2.2L7 5l2 1v2a1 1 0 0 1-1 1A7 7 0 0 1 1 2a1 1 0 0 1 1-1z" fill="#7a1414"/></svg>(866) 555-0147</li>
      <li><svg viewBox="0 0 10 10"><rect x="1" y="2.5" width="8" height="5.5" fill="none" stroke="#7a1414"/><path d="M1 2.5l4 3 4-3" fill="none" stroke="#7a1414"/></svg>sales@kestovatrading.ca</li>
      <li>www.kestovatrading.ca</li>
    </ul>
    <div class="rule"></div>
    <p class="address">1208-40 Harlow Ave, Toronto, ON, Canada M3J 2K7</p>
    <div class="tagline">International Flags &amp; Souvenirs</div>
  </section>

</body>
</html>
```